Home care agency

Current website QTRBLOOMS.com. Need to update and reformat to different pages. use my info from my current website

Target Market(s)

adult children

Industry/Entity Type

Home Health

Coding

Coded - Design and coding required

Number of Pages Required

4 page

Font styles to use
Sans Serif

Colors
3276b5
33a6d7
3277b5
85cae6
85acd3

```html
<!DOCTYPE html>
<html lang="en">
<head>
<meta charset="utf-8">
<title>QTR Blooms Health Services</title>
<link href="https://fonts.googleapis.com/css2?family=Montserrat:wght@400;500;600;700&family=Poppins:wght@300;400;500&display=swap" rel="stylesheet">
<style>
:root{
  --blue:#3276b5;
  --blue-deep:#1d5fa8;
  --sky:#33a6d7;
  --pale:#85cae6;
  --soft:#85acd3;
  --green:#5bb54a;
  --ink:#2b2b2b;
  --muted:#6d6d6d;
  --hero-bg:#ececec;
  --white:#ffffff;
}
*{margin:0;padding:0;box-sizing:border-box}
html,body{width:1200px;height:2924px;overflow:hidden;background:var(--white)}
body{font-family:"Montserrat",sans-serif;color:var(--ink);position:relative}
.section{position:absolute;left:0;width:1200px}

/* header */
.site-header{top:0;height:120px;background:var(--white)}
.brand{position:absolute;left:70px;top:34px;display:flex;align-items:center;gap:12px;font-weight:600;font-size:20px;color:var(--blue);letter-spacing:1px}
.brand-dot{width:44px;height:44px;border-radius:50%;border:3px solid var(--sky)}
.main-nav{position:absolute;right:70px;top:52px;display:flex;gap:56px;font-size:13px;font-weight:600;color:var(--blue);letter-spacing:.5px}
.main-nav a{color:inherit;text-decoration:none;position:relative}
.main-nav a.active{color:var(--green)}
.main-nav a.active::after{content:"";position:absolute;left:-18px;right:-18px;top:-52px;height:4px;background:var(--green)}

/* hero */
.hero{top:120px;height:680px;background:var(--hero-bg)}
.hero-photo{position:absolute;left:0;top:0;width:600px;height:680px;background:linear-gradient(135deg,#f6f6f6 0%,#dcdcdc 70%,#c9c9c9 100%)}
.hero-title{position:absolute;left:632px;top:172px;font-size:31px;font-weight:700;color:var(--blue);letter-spacing:.5px;white-space:nowrap}
.hero-tag{position:absolute;left:632px;top:226px;font-size:17px;font-weight:600;color:var(--green);letter-spacing:.5px;white-space:nowrap}
.btn{position:absolute;top:412px;width:220px;height:88px;display:flex;align-items:center;justify-content:center;font-size:13px;font-weight:600;letter-spacing:.5px;border-radius:4px}
.btn-primary{left:640px;background:var(--blue);color:var(--white)}
.btn-outline{left:888px;border:2px solid var(--blue);color:var(--blue)}

/* services */
.services{top:800px;height:780px;background:var(--blue-deep);color:var(--white)}
.section-title{position:absolute;left:0;width:1200px;text-align:center;font-size:48px;font-weight:400;letter-spacing:1px;line-height:1.2}
.services .section-title{top:88px;color:var(--white)}
.services .section-title::after{content:"";display:block;width:1040px;height:2px;background:rgba(255,255,255,.5);margin:20px auto 0}
.service{position:absolute;top:206px;width:320px}
.service-icon{width:196px;height:196px;border-radius:50%;border:6px solid var(--white);margin:0 auto;display:flex;align-items:center;justify-content:center}
.service h3{margin-top:32px;font-size:21px;font-weight:600;letter-spacing:.5px;text-align:center;white-space:nowrap}
.service ul{list-style:none;margin-top:28px;font-family:"Poppins",sans-serif;font-size:12.5px;line-height:1.4}
.service li{margin-bottom:25px}
.service li::before{content:"• "}
.s1{left:80px}.s2{left:440px}.s3{left:780px}

/* team */
.team{top:1580px;height:632px;background:var(--white)}
.team .section-title{top:86px;color:var(--blue)}
.team-photo{position:absolute;left:522px;top:180px;width:156px;height:156px;border-radius:50%;border:5px solid var(--blue);background:radial-gradient(circle at 50% 40%,#d8dde4,#8fa6c2)}
.arrow{position:absolute;top:292px;width:40px;height:40px;border-radius:50%;background:var(--blue-deep);display:flex;align-items:center;justify-content:center}
.arrow-left{left:92px}.arrow-right{left:1068px}
.team-text{position:absolute;left:190px;top:396px;width:820px;text-align:center;font-family:"Poppins",sans-serif;font-size:12px;line-height:2.2;color:var(--blue)}

/* mailing */
.mailing{top:2212px;height:148px;background:var(--blue-deep)}
.mailing h2{position:absolute;left:90px;top:50px;font-size:44px;font-weight:400;color:var(--white);letter-spacing:1px;white-space:nowrap}
.mailing h2 span{color:var(--green)}
.signup{position:absolute;left:720px;top:52px;width:340px;height:40px;background:var(--white);border-radius:3px;display:flex;align-items:center;padding-left:16px;font-family:"Poppins",sans-serif;font-size:11px;color:#9a9a9a}
.signup-go{position:absolute;right:4px;top:4px;width:40px;height:32px;background:var(--green);border-radius:3px;display:flex;align-items:center;justify-content:center}

/* footer */
.site-footer{top:2360px;height:564px;background:var(--white)}
.footer-links{position:absolute;top:14px;list-style:none;font-size:11px;font-weight:600;color:var(--blue);border-left:2px solid var(--soft);padding-left:22px}
.footer-links li{height:58px;display:flex;align-items:center}
.fl1{left:170px}.fl2{left:426px}
.area-map{position:absolute;left:760px;top:-20px;width:400px;height:440px;background:linear-gradient(160deg,#e9edf3 0%,#3f7cc0 45%,#1d5fa8 100%);border:1px solid var(--soft)}
.area-label{position:absolute;left:760px;top:448px;width:400px;text-align:center;font-size:17px;font-weight:600;color:var(--blue)}
.copyright{position:absolute;left:0;top:516px;width:1200px;border-top:2px solid var(--pale);padding-top:12px;padding-left:80px;font-size:9px;color:var(--muted)}
</style>
</head>
<body>

<header class="section site-header">
  <div class="brand"><span class="brand-dot"></span>QTR BLOOMS</div>
  <nav class="main-nav">
    <a class="active" href="#">HOME</a>
    <a href="#">SERVICES</a>
    <a href="#">CARE INQUIRY FORM</a>
    <a href="#">ABOUT</a>
    <a href="#">CONTACT</a>
  </nav>
</header>

<section class="section hero">
  <div class="hero-photo" role="img" aria-label="Photograph of a laboratory microscope on a white background"></div>
  <h1 class="hero-title">QTR BLOOMS HEALTH SERVICES</h1>
  <p class="hero-tag">PROVIDING CARE THROUGHOUT THE SOUTH SHORE</p>
  <a class="btn btn-primary">CONTACT</a>
  <a class="btn btn-outline">GET EMPLOYED</a>
</section>

<section class="section services">
  <h2 class="section-title">OUR SERVICES</h2>

  <div class="service s1">
    <div class="service-icon">
      <svg width="110" height="110" viewBox="0 0 110 110">
        <rect x="20" y="38" width="70" height="34" rx="17" fill="#fff" transform="rotate(-40 55 55)"/>
        <rect x="40" y="38" width="30" height="34" fill="#5bb54a" transform="rotate(-40 55 55)"/>
        <circle cx="50" cy="52" r="3" fill="#fff"/><circle cx="60" cy="58" r="3" fill="#fff"/>
      </svg>
    </div>
    <h3>SKILLED CARE SERVICES</h3>
    <ul>
      <li>Free Initial Nursing Assessment</li>
      <li>Medication Management</li>
      <li>Wound Care</li>
      <li>Injections</li>
      <li>Medical Care Assistance</li>
      <li>Transportation to Medical Appointments</li>
    </ul>
  </div>

  <div class="service s2">
    <div class="service-icon">
      <svg width="110" height="110" viewBox="0 0 110 110">
        <path d="M15 55 L55 20 L95 55" fill="none" stroke="#fff" stroke-width="8" stroke-linejoin="round"/>
        <rect x="28" y="52" width="54" height="40" fill="#fff"/>
        <rect x="38" y="60" width="12" height="12" fill="#5bb54a"/><rect x="60" y="60" width="12" height="12" fill="#5bb54a"/>
        <rect x="49" y="76" width="12" height="16" fill="#1d5fa8"/>
      </svg>
    </div>
    <h3>NON-MEDICAL SERVICES</h3>
    <ul>
      <li>Live-In Care</li>
      <li>Respite Care</li>
      <li>Assisting with Daily Living Activities</li>
      <li>Meal Preparations</li>
      <li>Companionship</li>
      <li>Homemaking</li>
    </ul>
  </div>

  <div class="service s3">
    <div class="service-icon">
      <svg width="110" height="110" viewBox="0 0 110 110">
        <circle cx="55" cy="30" r="11" fill="#fff"/>
        <rect x="43" y="44" width="24" height="24" rx="6" fill="#5bb54a"/>
        <path d="M15 78 Q40 70 60 78 L90 72 L90 84 L55 92 L15 88 Z" fill="#fff"/>
      </svg>
    </div>
    <h3>CLIENT BENEFITS</h3>
    <ul>
      <li>Continuity of care with same caregiver for each client on a regular basis</li>
      <li>Open communication with owner by phone or email</li>
      <li>Ongoing communications to client's family by phone or email on a weekly basis (if desired)</li>
    </ul>
  </div>
</section>

<section class="section team">
  <h2 class="section-title">THE TEAM</h2>
  <div class="team-photo" role="img" aria-label="Portrait photograph of a team member"></div>
  <div class="arrow arrow-left"><svg width="14" height="14" viewBox="0 0 14 14"><path d="M9 2 L4 7 L9 12" fill="none" stroke="#fff" stroke-width="2.5"/></svg></div>
  <div class="arrow arrow-right"><svg width="14" height="14" viewBox="0 0 14 14"><path d="M5 2 L10 7 L5 12" fill="none" stroke="#fff" stroke-width="2.5"/></svg></div>
  <p class="team-text">Our founder is a registered nurse with many years of home and hospital care experience. She understands the needs of families who want a loved one to stay safe and comfortable at home. Every caregiver is screened, trained and matched with care so that clients feel known and respected. We keep close contact with families and update the care plan as needs change over time.</p>
</section>

<section class="section mailing">
  <h2>JOIN OUR <span>MAILING</span> LIST</h2>
  <div class="signup">Enter your email
    <span class="signup-go"><svg width="16" height="16" viewBox="0 0 16 16"><path d="M1 8 L15 2 L11 15 L8 9 Z" fill="#fff"/></svg></span>
  </div>
</section>

<footer class="section site-footer">
  <ul class="footer-links fl1">
    <li>ABOUT US</li><li>OUR TEAM</li><li>PRIVACY POLICY</li><li>SERVICES</li><li>CARE INQUIRY</li>
  </ul>
  <ul class="footer-links fl2">
    <li>CONTACT US</li><li>MAILING ADDRESS</li><li>PAYMENT OPTIONS</li><li>CALL US</li>
  </ul>
  <div class="area-map" role="img" aria-label="Map of the service area with covered towns shaded blue"></div>
  <p class="area-label">SERVICE AREA</p>
  <p class="copyright">COPYRIGHT © 2024 QTR BLOOMS HEALTH SERVICES. ALL RIGHTS RESERVED.</p>
</footer>

</body>
</html>
```